Corvina
joyas
Corvina - Jewelry
Creative Brief
Jewelry
It is a company that sells jewerly, on line and in stores.
I like elegant, clean , proffesional and creative. I already have the logo, thanks
www.Lindenfold.example
I like the site lindenfold, and the concept a bit the same but in spanish, thanks

```html
<!DOCTYPE html>
<html lang="es">
<head>
<meta charset="utf-8">
<title>Corvina Joyas</title>
<link href="https://fonts.googleapis.com/css2?family=Arimo:wght@400;700&family=Cormorant+Garamond:wght@300&display=swap" rel="stylesheet">
<style>
:root{
  --page:#e6e7e8;
  --band:#cfe3ea;
  --ink:#333333;
  --muted:#666666;
  --dark:#2a2a2a;
  --nav-top:#4a4a4a;
  --nav-bottom:#151515;
  --accent:#d9c49a;
  --accent-dark:#b79c62;
  --panel:#f4f4f4;
  --panel-edge:#cfcfcf;
  --title-red:#8a1c1c;
  --footer:#2d2d2d;
}
*{margin:0;padding:0;box-sizing:border-box}
html,body{width:1200px;height:901px;overflow:hidden}
body{position:relative;background:var(--page);font-family:"Arimo",Arial,sans-serif;color:var(--ink)}
.band{position:absolute;left:0;top:97px;width:1200px;height:195px;background:var(--band)}
.header-ornament{position:absolute;top:8px;width:170px;height:80px;background:radial-gradient(ellipse at center,#b9b9b9 0%,rgba(185,185,185,0) 70%)}
.header-ornament.left{left:300px}
.header-ornament.right{left:730px}
.brand{position:absolute;left:0;top:30px;width:1200px;text-align:center;font-weight:700;font-size:38px;letter-spacing:2px;color:#4a4a4a}
.hero{position:absolute;left:263px;top:97px;width:674px;height:244px;background:linear-gradient(180deg,#fafafa 0%,#e4e4e4 100%);border:1px solid #d0d0d0}
.hero-photo{position:absolute;left:40px;top:0;width:360px;height:244px;background:radial-gradient(ellipse at 45% 45%,#d9b85a 0%,#e6d8b4 25%,rgba(240,240,240,0) 65%)}
.hero-quote{position:absolute;left:360px;top:135px;width:290px;font-size:11.5px;line-height:15px;color:#555;text-align:center}
.hero-word{position:absolute;left:20px;top:185px;font-family:"Cormorant Garamond",serif;font-weight:300;font-size:44px;letter-spacing:2px;color:#777}
.nav{position:absolute;left:263px;top:348px;width:674px;height:42px;background:linear-gradient(180deg,var(--nav-top),var(--nav-bottom));display:flex;align-items:center;padding-left:25px}
.nav a{color:#fff;text-decoration:none;font-size:12px;padding:0 13px;height:42px;line-height:42px;border-right:1px solid #555}
.nav a.active{background:linear-gradient(180deg,#e8d7b2,var(--accent-dark));color:#222}
.panel{position:absolute;background:var(--panel);border:1px solid var(--panel-edge);box-shadow:0 2px 4px rgba(0,0,0,.15)}
.panel-title{font-weight:700;font-size:12.5px;color:var(--dark);padding:8px 10px 6px;display:flex;align-items:center;gap:6px}
.panel-title::before{content:"";width:8px;height:8px;background:var(--dark)}
.category{left:263px;top:426px;width:187px;height:260px}
.category ul{list-style:none;padding:0 10px}
.category li{font-size:10px;color:#555;text-align:center;padding:4px 0;border-bottom:1px solid #dedede}
.newsletter{left:263px;top:706px;width:187px;height:97px}
.field{display:block;margin:2px 10px 4px;height:17px;border:1px solid #bbb;background:#fff;font-size:9.5px;line-height:15px;padding-left:5px;color:#555}
.submit{position:absolute;right:10px;bottom:8px;background:var(--dark);color:#fff;font-size:9.5px;padding:3px 9px}
.main{left:470px;top:426px;width:467px;height:395px}
.welcome{height:30px;background:linear-gradient(180deg,#5a5a5a,#2b2b2b);color:#fff;text-align:center;font-size:16px;line-height:30px}
.welcome b{font-weight:700}
.intro{font-size:9.5px;line-height:12.5px;color:#555;padding:7px 12px 0}
.best{position:absolute;left:14px;top:112px;font-size:14px;color:var(--title-red);display:flex;align-items:center;gap:6px}
.best::before{content:"";width:8px;height:8px;border-radius:50%;background:var(--title-red)}
.card{position:absolute;top:141px;width:100px;text-align:center}
.card-photo{height:53px;border:1px solid #ccc;background:linear-gradient(180deg,#ffffff,#e6e1d3)}
.card h3{font-size:8.5px;font-weight:700;margin-top:6px}
.card p{font-size:7.5px;line-height:9px;color:#666;margin-top:2px}
.card .price{font-size:8px;color:#444;text-align:right;margin-top:4px}
.card .buy{margin-top:4px;height:16px;background:linear-gradient(180deg,#555,#1e1e1e);color:#fff;font-size:8px;line-height:16px;text-align:left;padding-left:6px;position:relative}
.card .buy::after{content:"";position:absolute;right:4px;top:4px;width:8px;height:8px;background:var(--accent)}
.carousel{position:absolute;left:14px;top:292px;width:437px;height:92px;border-top:1px solid #ddd}
.arrow{position:absolute;top:36px;width:20px;height:20px}
.thumb{position:absolute;top:12px;width:80px;height:68px;border:1px solid #ccc;background:linear-gradient(180deg,#ffffff,#dcd8cc);box-shadow:0 1px 3px rgba(0,0,0,.2)}
.footer{position:absolute;left:0;top:832px;width:1200px;height:69px;background:linear-gradient(180deg,#3a3a3a,var(--footer))}
.footer-links{position:absolute;left:263px;top:22px;font-size:10px;color:#ddd}
.copyright{position:absolute;left:263px;top:38px;font-size:9px;color:#999}
.footer-brand{position:absolute;left:850px;top:22px;font-weight:700;font-size:18px;color:#8a8a8a;letter-spacing:1px}
</style>
</head>
<body>
<div class="band"></div>
<div class="header-ornament left" role="img" aria-label="Decorative swirl ornament"></div>
<div class="header-ornament right" role="img" aria-label="Decorative swirl ornament"></div>
<div class="brand">CORVINA</div>

<section class="hero">
  <div class="hero-photo" role="img" aria-label="Gold key pendant necklace with dark stone"></div>
  <p class="hero-quote">...Una llave de oro abre todas las cerraduras, ponte este collar como recordatorio de que todas las puertas estan abiertas para ti.</p>
  <div class="hero-word">LLAVE</div>
</section>

<nav class="nav">
  <a class="active">HOME</a><a>ABOUT US</a><a>JEWLRY</a><a>COLLECTION</a><a>GIFTS</a><a>FAQ</a><a>CONTACT US</a>
</nav>

<aside class="panel category">
  <div class="panel-title">JEWELERY CATEGORY</div>
  <ul>
    <li>Morbi varius nisi est</li>
    <li>Integer ultrices nisi ut</li>
    <li>Nullam aliquet lorem sit</li>
    <li>Curabitur iaculis egestas nunc</li>
    <li>Donec id massa vitae</li>
    <li>Phasellus sed dolor sed</li>
    <li>Donec sed augue sed</li>
    <li>Morbi fermentum felis non</li>
    <li>Vestibulum eget felis nec</li>
    <li>Suspendisse et nulla sit</li>
  </ul>
</aside>

<aside class="panel newsletter">
  <div class="panel-title">SIGNUP FOR NEWSLETTER</div>
  <span class="field">Name</span>
  <span class="field">E-mail</span>
  <span class="submit">Submit</span>
</aside>

<main class="panel main">
  <div class="welcome">Welcome to <b>CORVINA JOYAS</b></div>
  <p class="intro">Donec a massa tortor, ut iaculis massa. Etiam tristique sodales ligula, ac hendrerit turpis tincidunt sed. Suspendisse auctor rutrum massa sed faucibus.<br><br>Quisque sed neque, posuere id laoreet eget, tristique vel lorem. Sed vel dolor erat, in hendrerit lorem. Donec pellentesque ante a tellus semper interdum.</p>
  <div class="best">CORVINA Best Seller:</div>

  <div class="card" style="left:14px"><div class="card-photo" role="img" aria-label="Gold wishbone necklace"></div><h3>Piensa En Un Deseo</h3><p>Nulla facilisi. Curabitur vel dolor et justo tempus ut.</p><div class="price">Price: $199</div><div class="buy">Buy Now</div></div>
  <div class="card" style="left:126px"><div class="card-photo" role="img" aria-label="Gold cross pendant necklace"></div><h3>Piensa En Un Deseo</h3><p>Nulla facilisi. Curabitur vel dolor et justo tempus ut.</p><div class="price">Price: $199</div><div class="buy">Buy Now</div></div>
  <div class="card" style="left:238px"><div class="card-photo" role="img" aria-label="Delicate gold chain necklace"></div><h3>Piensa En Un Deseo</h3><p>Nulla facilisi. Curabitur vel dolor et justo tempus ut.</p><div class="price">Price: $199</div><div class="buy">Buy Now</div></div>
  <div class="card" style="left:352px"><div class="card-photo" role="img" aria-label="Silver charm necklace"></div><h3>Piensa En Un Deseo</h3><p>Nulla facilisi. Curabitur vel dolor et justo tempus ut.</p><div class="price">Price: $199</div><div class="buy">Buy Now</div></div>

  <div class="carousel">
    <svg class="arrow" style="left:6px" viewBox="0 0 20 20"><circle cx="10" cy="10" r="10" fill="#2a2a2a"/><path d="M12 5 L7 10 L12 15" stroke="#fff" stroke-width="2" fill="none"/></svg>
    <div class="thumb" style="left:46px" role="img" aria-label="Jewelry gift card product"></div>
    <div class="thumb" style="left:132px" role="img" aria-label="Necklace on display card"></div>
    <div class="thumb" style="left:218px" role="img" aria-label="Pendant on display card"></div>
    <div class="thumb" style="left:304px" role="img" aria-label="Necklace on display card"></div>
    <svg class="arrow" style="left:411px" viewBox="0 0 20 20"><circle cx="10" cy="10" r="10" fill="#2a2a2a"/><path d="M8 5 L13 10 L8 15" stroke="#fff" stroke-width="2" fill="none"/></svg>
  </div>
</main>

<footer class="footer">
  <div class="footer-links">Home &nbsp;|&nbsp; About Us &nbsp;|&nbsp; Jewelry &nbsp;|&nbsp; Collection &nbsp;|&nbsp; Gifts &nbsp;|&nbsp; FAQ &nbsp;|&nbsp; Contact Us</div>
  <div class="copyright">Copyright (C) CORVINA JOYAS. All rights reserved.</div>
  <div class="footer-brand">CORVINA</div>
</footer>
</body>
</html>
```